Painting Company Business Card

Brightwell Painting needs a new business card. See attachments for our logo and current card as an example.
We want to utilize the same colors in the logo, and keep all the information that is currently on it. Just need an updated and modern design.
We are open to loosing the Association Logos if it means a better design.
We are also entertaining a spot for a picture of a headshot of the person listed on the card. Head shot can be finished later.

```html
<!DOCTYPE html>
<html lang="en">
<head>
<meta charset="utf-8">
<title>Brightwell Painting – Business Card</title>
<link rel="stylesheet" href="https://fonts.googleapis.com/css2?family=Open+Sans:wght@400;600;700&display=swap">
<style>
  :root {
    --backdrop: #1a1a1a;
    --paint-brown: #6b3d3a;
    --paint-green: #3f4731;
    --paper: #ffffff;
    --ink: #1b1b1b;
    --badge: #2a2a2a;
    --divider: #111111;
  }
  html, body {
    margin: 0;
    width: 1200px;
    height: 1000px;
    overflow: hidden;
    background: var(--backdrop);
    font-family: "Open Sans", Arial, sans-serif;
  }
  .canvas { position: relative; width: 1200px; height: 1000px; }
  .card {
    position: absolute;
    top: 216px;
    width: 300px;
    height: 522px;
    display: flex;
    flex-direction: column;
    overflow: hidden;
  }
  .card--front { left: 137px; }
  .card--back { left: 706px; }
  .band { flex: none; }
  .band--brown { background: var(--paint-brown); }
  .band--green { background: var(--paint-green); }
  .band--paper { background: var(--paper); }
  .card--front .band--top { height: 34px; border-bottom: 2px solid var(--divider); }
  .card--front .band--body { flex: 1; position: relative; }
  .card--front .band--bottom { height: 32px; border-top: 2px solid var(--divider); }

  .wordmark {
    color: var(--paint-green);
    font-weight: 700;
    line-height: 1.05;
    display: flex;
    align-items: center;
    gap: 12px;
  }
  .wordmark__square { background: var(--paint-brown); flex: none; }
  .card--front .wordmark { position: absolute; left: 36px; top: 62px; font-size: 34px; }
  .card--front .wordmark__square { width: 22px; height: 80px; }

  .badges {
    position: absolute;
    left: 38px; top: 292px;
    display: grid;
    grid-template-columns: repeat(3, 46px);
    column-gap: 40px;
    row-gap: 14px;
  }
  .badge { background: var(--badge); justify-self: center; }
  .badge--tall { width: 44px; height: 70px; border-radius: 3px; }
  .badge--wide { width: 74px; height: 44px; border-radius: 3px; }
  .badge--mid { width: 40px; height: 62px; border-radius: 3px; }
  .badge--low { width: 58px; height: 42px; border-radius: 3px; }

  .card--back .band--top { height: 144px; display: flex; align-items: center; justify-content: center; }
  .card--back .wordmark { font-size: 22px; }
  .card--back .wordmark__square { width: 14px; height: 48px; }
  .card--back .band--contact { height: 248px; border-top: 2px solid var(--divider); border-bottom: 2px solid var(--divider); position: relative; color: var(--paper); }
  .card--back .band--services { flex: 1; }

  .person { position: absolute; left: 74px; top: 24px; font-variant: small-caps; }
  .person__name { font-size: 21px; font-weight: 600; letter-spacing: 0.5px; line-height: 1.1; }
  .person__role { font-size: 14px; letter-spacing: 0.5px; }

  .contacts { position: absolute; left: 40px; top: 96px; list-style: none; margin: 0; padding: 0; }
  .contact { display: flex; align-items: center; gap: 10px; height: 34px; margin-bottom: 8px; font-size: 14px; font-weight: 600; }
  .contact__icon { width: 34px; height: 34px; border-radius: 50%; background: var(--paper); display: flex; align-items: center; justify-content: center; }

  .services {
    list-style: none; margin: 0; padding: 32px 0 0 24px;
    display: grid; grid-template-columns: 160px 120px; row-gap: 12px;
    color: var(--paper); font-size: 12px; font-weight: 600; font-variant: small-caps; letter-spacing: 0.4px;
  }
  .service { display: flex; align-items: center; gap: 6px; font-size: 14px; }
  .service__box { width: 18px; height: 18px; border: 1px solid var(--paper); background: var(--paper); display: flex; align-items: center; justify-content: center; }
</style>
</head>
<body>
<main class="canvas">
  <section class="card card--front" aria-label="Card front">
    <div class="band band--brown band--top"></div>
    <div class="band band--paper band--body">
      <div class="wordmark"><span>Brightwell<br>Painting</span><span class="wordmark__square"></span></div>
      <div class="badges" aria-label="Association memberships">
        <span class="badge badge--tall"></span>
        <span class="badge badge--wide"></span>
        <span class="badge badge--mid"></span>
        <span class="badge badge--low"></span>
        <span class="badge badge--wide"></span>
        <span class="badge badge--low"></span>
      </div>
    </div>
    <div class="band band--green band--bottom"></div>
  </section>

  <section class="card card--back" aria-label="Card back">
    <div class="band band--paper band--top">
      <div class="wordmark"><span>Brightwell<br>Painting</span><span class="wordmark__square"></span></div>
    </div>
    <div class="band band--green band--contact">
      <div class="person">
        <div class="person__name">Daniel Harper</div>
        <div class="person__role">Quality Manager</div>
      </div>
      <ul class="contacts">
        <li class="contact">
          <span class="contact__icon"><svg width="18" height="18" viewBox="0 0 24 24"><path d="M6.6 2.5l3 3.6-1.9 2.2a13 13 0 006 6l2.2-1.9 3.6 3-2 3.4C10 18.6 5.4 14 3.2 6.5z" fill="#1b1b1b"/></svg></span>
          262-555-0148
        </li>
        <li class="contact">
          <span class="contact__icon"><svg width="20" height="16" viewBox="0 0 20 16"><rect x="1" y="2" width="18" height="12" fill="none" stroke="#1b1b1b" stroke-width="1.6"/><path d="M1 2l9 7 9-7" fill="none" stroke="#1b1b1b" stroke-width="1.6"/></svg></span>
          Daniel.Brightwell@mail.com
        </li>
        <li class="contact">
          <span class="contact__icon"><svg width="20" height="20" viewBox="0 0 20 20" fill="none" stroke="#1b1b1b" stroke-width="1.4"><circle cx="10" cy="10" r="8"/><ellipse cx="10" cy="10" rx="3.5" ry="8"/><path d="M2 10h16M3.5 5.5h13M3.5 14.5h13"/></svg></span>
          BrightwellPainting.com
        </li>
      </ul>
    </div>
    <div class="band band--brown band--services">
      <ul class="services">
        <li class="service"><span class="service__box"><svg width="14" height="14" viewBox="0 0 14 14"><path d="M2 7l3.5 4L12 2" fill="none" stroke="#6b3d3a" stroke-width="2.4"/></svg></span>Exterior Painting</li>
        <li class="service"><span class="service__box"><svg width="14" height="14" viewBox="0 0 14 14"><path d="M2 7l3.5 4L12 2" fill="none" stroke="#6b3d3a" stroke-width="2.4"/></svg></span>Carpentry</li>
        <li class="service"><span class="service__box"><svg width="14" height="14" viewBox="0 0 14 14"><path d="M2 7l3.5 4L12 2" fill="none" stroke="#6b3d3a" stroke-width="2.4"/></svg></span>Interior Painting</li>
        <li class="service"><span class="service__box"><svg width="14" height="14" viewBox="0 0 14 14"><path d="M2 7l3.5 4L12 2" fill="none" stroke="#6b3d3a" stroke-width="2.4"/></svg></span>Drywall</li>
      </ul>
    </div>
  </section>
</main>
</body>
</html>
```